Crestwell Flue Sweeping- needs a clean, simple easy to use website

We are a small family run business,running for approximately 18 months, providing chimney sweeping services within a 50 mile radius of our base.
Crestwell Flue Sweeping is certified through The Order of Senior Hearth Cleaners - the Order is both nationally and internationally recognised for its efforts and achievements in improving standards for both chimney sweeps and their customers.
We would describe our company as:
Professional, friendly, customer oriented, safety concious, enthusiastic. Clean and thorough, with a high level of knowledge.
We believe in setting high standards in our industry and providing our customers with an easy and positive experience.
Through our site we aim to increase traffic and generate more sales, create awareness of our company, advertise and inform of our services.
Our target audience is adult home owners, landlords, tenants and letting agencies and the website should be able to be accessed via phone, tablet and PC.
We would like to see designs using black, white and grey apart from our logo (attached) which is yellow.
We would be open to suggestion on a small amount of colour.

We would like to see some designs with silhouette terraced house roof tops with chimneys and with our logo and chimney sweep to the left side as on our van.

Examples of our competitors sites:
www.tallowby-fluecare.co.uk
www.pennick.co.uk
www.greenhearthandnest.com
www.uplandburners.co.uk

Some examples of website designs we like:
www.polishpro.co.uk
www.swiftlet.properties
www.brindlemeadow.com

The site should include the following pages each page to follow the same template/design as the homepage but with spaces allocated for the relevant information for each page.
Home/about page
Chimney Sweeping
Other Services
Fire Safety
Contact Us

It should also have the facility to display a map showing the area we cover and photos of our work.

To conclude the final design should communicate ease of use, cleanliness and professionalism.

NB; We also do window cleaning but don't want this on the website

Target Market(s)

As in project description

Industry/Entity Type

Business

Coding

Coded - Design and coding required

Number of Pages Required

5+ page

Font styles to use
Sans Serif

Requirements
Must have
• Pages as mentioned in the design brief.
• Company logo (as on van)
• Order of senior hearth cleaners logo
• Parvo logo to be added in (on training course in just over 1 week)
Nice to have
• possibly some chimneys in clipart/silhouette
Should not have
• Too much colour or too busy

```html
<!DOCTYPE html>
<html lang="en">
<head>
<meta charset="utf-8">
<title>Crestwell Flue Sweeping</title>
<link href="https://fonts.googleapis.com/css2?family=Open+Sans:wght@300;400;600;700&family=Dancing+Script:wght@600&display=swap" rel="stylesheet">
<style>
:root{
  --yellow:#fff200;
  --ink:#1c1c1c;
  --bar:#141414;
  --panel:#2e2e2e;
  --grey-band:#ececec;
  --text:#555;
  --white:#fff;
}
*{margin:0;padding:0;box-sizing:border-box}
html,body{width:1200px;height:2236px;overflow:hidden}
body{position:relative;background:var(--white);font-family:"Open Sans",sans-serif;color:var(--text)}
.abs{position:absolute}

/* header */
.topbar{left:0;top:0;width:1200px;height:100px;background:var(--bar)}
.brand{left:110px;top:0;width:240px;height:100px;background:var(--yellow);display:flex;align-items:center;justify-content:center;gap:12px}
.brand-mark{width:22px;height:22px;border-radius:50%;background:var(--ink)}
.brand-name{font-weight:700;font-size:22px;letter-spacing:2px;color:var(--ink)}
.main-nav{right:100px;top:0;height:100px;display:flex;align-items:center;gap:30px}
.main-nav a{color:#ddd;text-decoration:none;font-size:13px;font-weight:600;letter-spacing:.5px;text-transform:uppercase}
.main-nav a.active{color:var(--yellow)}

/* hero */
.hero{left:0;top:100px;width:1200px;height:520px;background:linear-gradient(180deg,#8da3b8 0%,#6e6256 35%,#4a3a2e 70%,#3b3836 100%)}
.contact-strip{left:100px;top:540px;width:1000px;height:140px}
.info-box{top:0;height:140px;width:340px;background:var(--panel);color:#ccc;padding:34px 30px;display:flex;gap:18px}
.info-box.locator{left:0}
.info-box.message{right:0}
.info-box h3{font-size:22px;font-weight:400;color:var(--white);text-transform:uppercase;letter-spacing:1px}
.info-box p{font-size:12px;margin-top:6px;text-transform:uppercase;line-height:1.5}
.call-box{left:340px;top:-50px;width:320px;height:210px;background:var(--yellow);text-align:center;padding-top:40px;color:var(--ink)}
.call-box .label{font-size:15px;margin-top:10px;text-transform:uppercase;letter-spacing:1px}
.call-box .number{font-size:34px;font-weight:400}

/* welcome */
.section-title{width:1200px;left:0;text-align:center;font-weight:300;font-size:38px;color:var(--ink);text-transform:uppercase}
.section-title strong{font-weight:700;color:var(--ink)}
.welcome-title{top:735px}
.title-rule{left:560px;width:80px;height:3px;background:var(--yellow)}
.welcome-copy{left:170px;top:815px;width:860px;font-size:14px;line-height:1.75;text-align:center}

.services{left:168px;top:920px;width:864px;display:flex;gap:32px}
.service{width:192px}
.service-photo{height:212px}
.service-label{height:40px;background:var(--yellow);color:var(--ink);font-size:12px;font-weight:700;display:flex;align-items:center;justify-content:center;text-transform:uppercase}

/* testimonial */
.testimonial{left:0;top:1240px;width:1200px;height:210px;background:var(--grey-band)}
.quote-text{left:200px;top:1290px;width:800px;text-align:center;font-size:15px;line-height:1.8;font-style:italic}
.quote-author{left:0;width:1200px;top:1390px;text-align:center;font-family:"Dancing Script",cursive;font-size:28px;color:#444}

/* projects */
.projects-title{top:1505px}
.projects{left:200px;top:1590px;width:800px;height:220px;display:flex;gap:6px}
.project{flex:1}

/* map & footer */
.area-map{left:0;top:1850px;width:1200px;height:310px;background:linear-gradient(135deg,#e8e3d4 0%,#d9e2c8 40%,#efe6c9 70%,#dcd7cc 100%)}
.footer{left:0;top:2160px;width:1200px;height:76px;background:var(--bar);display:flex;align-items:center;justify-content:space-between;padding:0 30px}
.copyright{font-size:12px;color:#aaa}
.social{display:flex;gap:8px}
.social span{width:26px;height:26px;background:var(--yellow)}
</style>
</head>
<body>

<header class="abs topbar"></header>
<div class="abs brand"><span class="brand-mark"></span><span class="brand-name">CRESTWELL</span></div>
<nav class="abs main-nav">
  <a class="active" href="#">Home</a>
  <a href="#">About Page</a>
  <a href="#">Chimney Sweeping</a>
  <a href="#">Other Services</a>
  <a href="#">Fire Safety</a>
  <a href="#">Contact Us</a>
</nav>

<div class="abs hero" role="img" aria-label="Photo of a chimney sweep at work outside a timber-clad house with the company van"></div>

<section class="abs contact-strip">
  <div class="abs info-box locator">
    <svg width="34" height="44" viewBox="0 0 34 44"><path d="M17 2C9 2 3 8 3 16c0 10 14 26 14 26s14-16 14-26C31 8 25 2 17 2z" fill="none" stroke="#fff" stroke-width="3"/><circle cx="17" cy="16" r="5" fill="#fff"/></svg>
    <div><h3>Locator</h3><p>12 Ember Row,<br>Hollin Vale</p></div>
  </div>
  <div class="abs call-box">
    <svg width="26" height="42" viewBox="0 0 26 42"><rect x="2" y="2" width="22" height="38" rx="4" fill="none" stroke="#1c1c1c" stroke-width="3"/><circle cx="13" cy="33" r="2.5" fill="#1c1c1c"/></svg>
    <div class="label">Call us now!</div>
    <div class="number">+1 800 555 0142</div>
  </div>
  <div class="abs info-box message">
    <svg width="44" height="34" viewBox="0 0 44 34"><rect x="2" y="2" width="40" height="30" fill="none" stroke="#fff" stroke-width="3"/><path d="M2 2l20 16L42 2" fill="none" stroke="#fff" stroke-width="3"/></svg>
    <div><h3>Message</h3><p>Send us a note<br>any time</p></div>
  </div>
</section>

<h2 class="abs section-title welcome-title">Welcome to <strong>Crestwell</strong></h2>
<div class="abs title-rule" style="top:795px"></div>
<p class="abs welcome-copy">We are a small family run chimney sweeping business covering homes within fifty miles of our base. Every sweep is clean, thorough and safety checked, with dust sheets, a full inspection and a certificate on completion. We work with home owners, landlords, tenants and letting agencies, and we always arrive on time and leave your room spotless.</p>

<section class="abs services">
  <div class="service"><div class="service-photo" role="img" aria-label="Photo of a wood burning stove being serviced" style="background:linear-gradient(160deg,#d9d4cc,#6d6259)"></div><div class="service-label">Stove Servicing</div></div>
  <div class="service"><div class="service-photo" role="img" aria-label="Photo of a sweep working on a chimney" style="background:linear-gradient(160deg,#6fa4d6,#2d3c4a)"></div><div class="service-label">Chimney Sweeping</div></div>
  <div class="service"><div class="service-photo" role="img" aria-label="Photo of a smoke alarm fitted on a ceiling" style="background:linear-gradient(160deg,#9fd1f0,#2f7bb5)"></div><div class="service-label">Fire Safety</div></div>
  <div class="service"><div class="service-photo" role="img" aria-label="Photo of a roofline with chimneys against the sky" style="background:linear-gradient(160deg,#bfe0f5,#4f86b3)"></div><div class="service-label">Tips &amp; Advice</div></div>
</section>

<section class="abs testimonial"></section>
<p class="abs quote-text">Friendly, punctual and incredibly tidy. The sweep explained every step, checked the flue thoroughly and left the living room cleaner than before. We will book again next autumn without a second thought.</p>
<p class="abs quote-author">- Ava Marsh</p>

<h2 class="abs section-title projects-title">Latest <strong>Projects</strong></h2>
<div class="abs title-rule" style="top:1565px"></div>
<section class="abs projects">
  <div class="project" role="img" aria-label="Photo of a fireplace after sweeping" style="background:linear-gradient(160deg,#d8d4cc,#7d7367)"></div>
  <div class="project" role="img" aria-label="Photo of company vans" style="background:linear-gradient(160deg,#f4f4f4,#c9c9c9)"></div>
  <div class="project" role="img" aria-label="Photo of a house exterior after a job" style="background:linear-gradient(160deg,#cfd6dc,#5d6670)"></div>
  <div class="project" role="img" aria-label="Photo of the team beside the company van" style="background:linear-gradient(160deg,#e8e3b0,#3a3a3a)"></div>
</section>

<div class="abs area-map" role="img" aria-label="Map of the area covered by the service"></div>

<footer class="abs footer">
  <span class="copyright">© 2013 Crestwell Flue Sweeping. All rights reserved</span>
  <div class="social"><span></span><span></span><span></span><span></span><span></span></div>
</footer>

</body>
</html>
```